Flyer for promoting a hotel in the beach in miami for an event

We are are KT Harbor and have a resort at Miami, Hallandale Beach.
We need a triptych:
- With a lot of photos to show the clients the wonderful experience they can live with their families going on vacations to miami.
- We want the amenities and photos of the units to stand out.
I attached a document called Triptico that is a guide for you to know what we want, and another called . When you do your design you must know that:
- The text should be linked to each photo. All the photos are attached.
- There is freedom to play with the structure. I did an example, but PLEASE mix this up and do it less structured.
- You can feel free to add any other photos at the background, from the ones I sent or from other places. Like for example of a family.

Target Market(s)

Families who go to vacaton to have a great experience and memories. Targeted to people who love the beach and miami

Industry/Entity Type

Hotel

Font styles to use
Sans Serif

Colors
ec1f27
ffffff

Requirements
Must have
• The photos with numbers

```html
<!DOCTYPE html>
<html lang="en">
<head>
<meta charset="utf-8">
<title>KT Harbor – Hallandale Beach Stays</title>
<link href="https://fonts.googleapis.com/css2?family=PT+Sans:wght@400;700&family=PT+Sans+Narrow:wght@700&display=swap" rel="stylesheet">
<style>
  :root{
    --red:#ec1f27;
    --white:#ffffff;
    --sand:#e4ddd2;
    --stone:#c9c3bb;
    --grey-veil:#b9b6b1;
    --fold:#6d6a66;
    --teal:#9fcfc2;
    --teal-edge:#86c2b3;
    --ink:#2f2f2f;
  }
  *{box-sizing:border-box;margin:0;padding:0}
  html,body{width:1200px;height:848px;overflow:hidden;background:var(--sand)}
  body{font-family:"PT Sans",Arial,sans-serif;color:var(--ink)}
  .brochure{position:relative;width:1200px;height:848px;overflow:hidden;background:var(--sand)}

  /* backdrop */
  .backdrop-city{position:absolute;left:0;top:0;width:402px;height:848px;
    background:linear-gradient(170deg,#c3c9cc 0%,#d7d3cc 25%,#b9c3c4 45%,#d9cdb6 70%,#cdbf9f 100%)}
  .backdrop-beach{position:absolute;left:330px;top:120px;width:560px;height:728px;
    background:linear-gradient(115deg,#8bb3c2 0%,#9ec3c6 18%,#c7c4b0 34%,#d8c8a6 55%,#cdb793 78%,#bfa986 100%)}
  .backdrop-right{position:absolute;left:804px;top:0;width:396px;height:848px;
    background:linear-gradient(165deg,#e7e1d8 0%,#ece7e0 50%,#d9d3ca 100%)}
  .veil{position:absolute;left:0;top:0;width:1200px;height:848px}
  .fold{position:absolute;top:0;width:3px;height:848px;background:var(--fold)}

  /* unit cards */
  .unit{position:absolute;left:17px;width:376px;height:197px}
  .unit-price{position:absolute;left:0;top:0;width:141px;height:197px;background:var(--teal);border:2px solid var(--teal-edge)}
  .unit-info{position:absolute;left:154px;top:0;width:222px;height:197px;background:var(--teal);border:2px solid var(--teal-edge)}
  .tab{position:absolute;left:-2px;top:20px;width:141px;height:23px;background:var(--red);color:var(--white);
    font:400 15px/23px "PT Sans",Arial,sans-serif;padding-left:9px;letter-spacing:.2px}
  .unit-photo{position:absolute;left:0;top:43px;width:92px;height:66px}
  .prices{position:absolute;left:0;right:0;top:118px;text-align:center;font-size:14px;line-height:21px;color:#333}
  .info-head{position:absolute;left:-2px;top:20px;width:222px;height:23px;color:var(--white);
    background:linear-gradient(90deg,var(--red) 0,var(--red) 72%,rgba(236,31,39,.35) 100%);
    font:700 16px/23px "PT Sans Narrow",Arial,sans-serif;padding-left:9px}
  .features{position:absolute;left:12px;top:54px;right:4px;list-style:none}
  .features li{position:relative;padding-left:22px;font-size:15.5px;line-height:21px;margin-bottom:2px;color:#333}
  .features svg{position:absolute;left:0;top:5px;width:13px;height:12px}

  /* captions & photos */
  .banner{position:absolute;background:var(--red);color:var(--white);text-align:center}
  .photo{position:absolute;border:5px solid var(--teal)}
  .title{font:700 16px/25px "PT Sans",Arial,sans-serif}
  .caption{font-size:12px;line-height:15px;padding:6px 10px}
</style>
</head>
<body>
<main class="brochure">
  <div class="backdrop-city" role="img" aria-label="Faint view of Miami high-rise skyline above the beach"></div>
  <div class="backdrop-beach" role="img" aria-label="Aerial view of Hallandale beach with turquoise sea and sand"></div>
  <div class="backdrop-right"></div>
  <svg class="veil" viewBox="0 0 1200 848" aria-hidden="true">
    <polygon points="402,0 800,0 800,40 660,0 560,0 800,180 800,210 402,215" fill="#bdb9b3" opacity=".85"/>
    <polygon points="560,0 660,0 800,40 800,180" fill="#e6e1da" opacity=".9"/>
    <polygon points="804,560 840,560 840,848 804,848" fill="#9fa3a2" opacity=".55"/>
    <polygon points="804,330 880,360 880,560 804,560" fill="#c9bfae" opacity=".6"/>
    <polygon points="0,0 150,0 0,120" fill="#d9d6d1" opacity=".6"/>
  </svg>
  <div class="fold" style="left:401px"></div>
  <div class="fold" style="left:801px"></div>

  <svg width="0" height="0" style="position:absolute">
    <symbol id="tick" viewBox="0 0 13 12"><path d="M1 8 L4 11 L12 1" fill="none" stroke="#ec1f27" stroke-width="2.2"/></symbol>
  </svg>

  <!-- units -->
  <section class="unit" style="top:17px">
    <div class="unit-price">
      <div class="tab">STARTING FROM</div>
      <div class="unit-photo" role="img" aria-label="Studio bedroom with white bedding and navy headboard"
           style="background:linear-gradient(120deg,#4a5f86 0%,#9aa8bf 30%,#f2f2f4 55%,#d9d6d2 80%,#8d8a86 100%)"></div>
      <p class="prices">$ 119.00/DAY<br>$ 699.00/WEEK<br>$ 2,099.00/MONTH</p>
    </div>
    <div class="unit-info">
      <div class="info-head">STUDIO /ONE BATHROOM</div>
      <ul class="features">
        <li><svg><use href="#tick"/></svg>Intracoastal waterway view</li>
        <li><svg><use href="#tick"/></svg>Accommodates : 2</li>
        <li><svg><use href="#tick"/></svg>Maximum capacity : 4</li>
      </ul>
    </div>
  </section>

  <section class="unit" style="top:225px">
    <div class="unit-price">
      <div class="tab">STARTING FROM</div>
      <div class="unit-photo" role="img" aria-label="Studio kitchen with white cabinets and steel appliances"
           style="background:linear-gradient(100deg,#f4f4f3 0%,#d8d8d6 35%,#7c7f83 55%,#e9e8e5 75%,#b7b4ae 100%)"></div>
      <p class="prices">$ 149.00/DAY<br>$ 899.00/WEEK<br>$ 2,699.00/MONTH</p>
    </div>
    <div class="unit-info">
      <div class="info-head">STUDIO /ONE BATHROOM</div>
      <ul class="features">
        <li><svg><use href="#tick"/></svg>Intracoastal waterway view</li>
        <li><svg><use href="#tick"/></svg>Accommodates : 2</li>
        <li><svg><use href="#tick"/></svg>Maximum capacity : 3</li>
        <li><svg><use href="#tick"/></svg>Fully Equipped Kitchen, washer &amp; dryer</li>
      </ul>
    </div>
  </section>

  <section class="unit" style="top:432px">
    <div class="unit-price">
      <div class="tab">STARTING FROM</div>
      <div class="unit-photo" role="img" aria-label="Living room with blue sofa and window view"
           style="background:linear-gradient(160deg,#e8ecef 0%,#c9d3dc 35%,#2f5d8a 60%,#9fb1c4 80%,#d8d2c7 100%)"></div>
      <p class="prices">$ 229.00/DAY<br>$ 1,399.00/WEEK<br>$ 4,099.00/MONTH</p>
    </div>
    <div class="unit-info">
      <div class="info-head">STUDIO /ONE BATHROOM</div>
      <ul class="features">
        <li><svg><use href="#tick"/></svg>Intracoastal waterway view</li>
        <li><svg><use href="#tick"/></svg>Accommodates : 4</li>
        <li><svg><use href="#tick"/></svg>Maximum capacity : 6</li>
        <li><svg><use href="#tick"/></svg>Fully Equipped Kitchen, washer &amp; dryer</li>
      </ul>
    </div>
  </section>

  <section class="unit" style="top:641px">
    <div class="unit-price">
      <div class="tab">STARTING FROM</div>
      <div class="unit-photo" role="img" aria-label="Bedroom with white bed and teal rug"
           style="background:linear-gradient(170deg,#e9e6e0 0%,#f6f5f3 40%,#bfbab3 62%,#3f9aa0 82%,#2b7b84 100%)"></div>
      <p class="prices">$ 399.00/DAY<br>$ 2,290.00/WEEK<br>$ 6,899.00/MONTH</p>
    </div>
    <div class="unit-info">
      <div class="info-head">STUDIO /ONE BATHROOM</div>
      <ul class="features">
        <li><svg><use href="#tick"/></svg>Intracoastal waterway view</li>
        <li><svg><use href="#tick"/></svg>Accommodates : 6</li>
        <li><svg><use href="#tick"/></svg>Maximum capacity : 7</li>
        <li><svg><use href="#tick"/></svg>Fully Equipped Kitchen, washer &amp; dryer</li>
      </ul>
    </div>
  </section>

  <!-- beach club -->
  <div class="banner title" style="left:446px;top:36px;width:316px;height:25px">PREMIUM BEACH CLUB</div>
  <div class="photo" role="img" aria-label="White beach club building with palm trees under blue sky"
       style="left:450px;top:64px;width:308px;height:112px;background:linear-gradient(100deg,#f1eff0 0%,#c9c3cf 20%,#5c4a7a 32%,#e9ecef 45%,#2f7fd0 62%,#3f8a3c 78%,#2a6fc7 100%)"></div>
  <div class="photo" role="img" aria-label="Pool deck with red loungers beside the tower"
       style="left:450px;top:184px;width:308px;height:110px;background:linear-gradient(175deg,#2e7fd6 0%,#9ccbee 28%,#e8eef2 45%,#c9302f 60%,#29b3d6 75%,#c7c3bb 100%)"></div>
  <div class="banner caption" style="left:450px;top:321px;width:308px;height:96px;padding-top:12px">
    Free access to the Dune Beach Club (at the beach where you can enjoy beach chairs, towels and umbrellas for no additional cost (subject to availability). It also provides cocktails, premium dishes and much more.</div>
  <div class="photo" role="img" aria-label="White beach umbrellas and red loungers on the sand by turquoise sea"
       style="left:450px;top:420px;width:308px;height:178px;background:linear-gradient(170deg,#2e86dc 0%,#f4f5f6 28%,#dfe4e6 45%,#27b7c9 60%,#c8352f 74%,#e3d3b3 88%,#d2bb92 100%)"></div>
  <div class="banner caption" style="left:450px;top:617px;width:308px;height:34px;line-height:22px">Free Beach&nbsp; Club Access and chairs just for you!</div>
  <div class="photo" role="img" aria-label="Beach loungers with umbrellas and palms on white sand"
       style="left:450px;top:653px;width:308px;height:173px;background:linear-gradient(175deg,#3b8fe0 0%,#b9d9f2 30%,#4c8a4a 45%,#2a5f8f 60%,#efe7d6 75%,#d9c6a2 100%)"></div>

  <!-- amenities -->
  <div class="banner caption" style="left:848px;top:36px;width:298px;height:54px;padding-top:10px">One block ride to the beach,<br>back and forth, every few minutes!</div>
  <div class="photo" role="img" aria-label="Electric shuttle cart driving beside the hotel tower"
       style="left:848px;top:88px;width:298px;height:190px;background:linear-gradient(170deg,#2f86e0 0%,#8cc4ee 35%,#3e8a48 55%,#d9d9d6 70%,#c9b9a6 85%,#b23a32 100%)"></div>
  <div class="banner caption" style="left:848px;top:296px;width:298px;height:70px;padding-top:5px;line-height:14px">
    Infinity pool by Marlowe alongside the<br>the Intracoastal waterway<br>Chase Lounge<br>Towel Service</div>
  <div class="photo" role="img" aria-label="Hotel tower with infinity pool along the water"
       style="left:848px;top:363px;width:298px;height:186px;background:linear-gradient(100deg,#dfe3e7 0%,#f6f6f6 25%,#9aa3ab 42%,#3a86d6 60%,#3d7e3f 78%,#2fa5d2 100%)"></div>
  <div class="banner caption" style="left:848px;top:567px;width:298px;height:53px;line-height:40px">Water taxi job!</div>
  <div class="photo" role="img" aria-label="Yellow water taxi docked on the Intracoastal with city towers behind"
       style="left:848px;top:623px;width:298px;height:197px;background:linear-gradient(175deg,#2f85dc 0%,#a7cdee 30%,#d5d6d3 45%,#2f6f9b 62%,#e3c12a 75%,#c8ae7c 100%)"></div>
</main>
</body>
</html>
```